We specialize in pizza, pasta and salads and are now offering TAKE & BAKE and GRAB & GO ...

Looking for either a 8.5" x 11" or similar for a instore display. WILL BE ON A SWIVELING HOLDER to catch customers attention.

**THIS IS A DOUBLE SIDED PRINT**

ONE SIDE will consist of WHAT'S FOR DINNER TONIGHT? and the following:
* Take & Bake"
* "Baked Pasta"
* Freshly made in house
* Lasagna
$13.50
- please include attached closeup picture and logo

THE OTHER SIDE will consist of
mini charcutier board.
* snack size charcutier delight *
* Enjoy the flavors of gourmet snacking, all in one convenient box!

PRICE $8.99

Winning design will be commissioned to design labels for "grab and go" for take and bake pasta, charcuterie box, pasta salads, candy etc.

Thank you and please do not hesitate to ask any questions.

www.calderipizza.ca
www.fernloop.ca
Logo to be interchanged as they are affiliated meaning FernLoop is a brand within Calderi pizza.

Target Market(s)

our target market is customers who have already entered our business. This is to upsel

Industry/Entity Type

We are in a self serve enviroment and target business people

Requirements
Must have
• must be clean and catchy. We are located in a professional business community.
Nice to have
• Must be appealing, appetizing and utilize our website colors
Should not have
• should not have any carton drawings and not be cluttered (busy)

```html
<!DOCTYPE html>
<html lang="en">
<head>
<meta charset="utf-8">
<title>Calderi pizza – In-store Display Posters</title>
<link rel="stylesheet" href="https://fonts.googleapis.com/css2?family=Montserrat:wght@600;700;800;900&family=Sniglet:wght@800&display=swap">
<style>
  :root {
    --navy: #111842;
    --navy-deep: #0b1030;
    --orange: #ef4e23;
    --red: #b0202b;
    --white: #ffffff;
    --ink: #1b1f3b;
    --band-low: #e2e3e5;
  }
  * { box-sizing: border-box; margin: 0; padding: 0; }
  html, body { width: 1200px; height: 4571px; overflow: hidden; }
  body { font-family: "Montserrat", sans-serif; background: var(--band-low); position: relative; }

  .band { position: absolute; left: 0; width: 1200px; }
  .band--one { top: 0; height: 945px; background: linear-gradient(#cbcbcb, #dadada); }
  .band--two { top: 945px; height: 1170px; background: linear-gradient(#cacaca, #d8d8d8); }
  .band--three { top: 2115px; height: 2456px; background: var(--band-low); }

  .slot { position: absolute; }
  .slot--small { width: 335px; height: 432px; left: 432px; }
  .slot--small .poster { transform: scale(0.45); transform-origin: 0 0; }
  .slot--a { top: 256px; }
  .slot--b { top: 1314px; }
  .slot--c { top: 2330px; left: 228px; width: 744px; height: 960px; }
  .slot--d { top: 3340px; left: 228px; width: 744px; height: 960px; }

  .poster {
    position: relative; width: 744px; height: 960px; overflow: hidden;
    background: var(--navy); box-shadow: 6px 8px 0 rgba(0,0,0,0.12);
  }
  .poster__ghost {
    position: absolute; left: 0; right: 0; top: 0;
    font-weight: 900; font-size: 150px; line-height: 118px;
    color: rgba(255,255,255,0.05); text-align: center; letter-spacing: 4px;
  }
  .poster__photo { position: absolute; left: 0; width: 744px; }
  .poster__photo--fondue {
    top: 290px; height: 580px;
    background:
      radial-gradient(ellipse at 55% 85%, #c7741f 0%, #9a4c17 22%, transparent 45%),
      radial-gradient(ellipse at 30% 55%, #e7ddd0 0%, #b9b6b9 40%, transparent 70%),
      linear-gradient(#111842 0%, #3b3f63 18%, #d9d3cc 45%, #cfc6bb 100%);
  }
  .poster__photo--board {
    top: 342px; height: 543px;
    background:
      radial-gradient(circle at 75% 45%, #c21f2a 0%, transparent 22%),
      radial-gradient(circle at 30% 80%, #3a2f5c 0%, transparent 18%),
      radial-gradient(circle at 18% 35%, #e6d9b0 0%, transparent 20%),
      linear-gradient(135deg, #8c5a2b, #d9a35a 40%, #a8743c 70%, #6b4522);
  }

  .headline { position: absolute; left: 0; top: 0; width: 744px; height: 380px; overflow: visible; }
  .headline__kicker { font-family: "Montserrat", sans-serif; font-weight: 900; fill: var(--orange); }
  .headline__kicker--outlined {
    stroke: var(--white); stroke-width: 6px; paint-order: stroke;
    stroke-linejoin: round; filter: drop-shadow(0 6px 6px rgba(0,0,0,0.45));
  }
  .headline__hero {
    font-family: "Sniglet", sans-serif; font-weight: 800; fill: var(--white);
    stroke: var(--navy-deep); stroke-width: 10px; paint-order: stroke; stroke-linejoin: round;
    filter: drop-shadow(0 7px 6px rgba(0,0,0,0.55));
  }

  .price {
    position: absolute; border-radius: 50%; background: var(--red); color: var(--white);
    display: flex; flex-direction: column; align-items: center; justify-content: center;
    font-weight: 800; box-shadow: 0 6px 14px rgba(0,0,0,0.3);
  }
  .price__label { font-size: 31px; line-height: 32px; }
  .price__value { font-size: 44px; line-height: 46px; }
  .price__value sup { font-size: 17px; vertical-align: 18px; margin-right: 3px; }
  .dinner .price { left: 52px; top: 530px; width: 166px; height: 166px; }
  .snack .price { left: 502px; top: 368px; width: 176px; height: 176px; }

  .tags { position: absolute; left: 52px; top: 808px; display: flex; list-style: none; }
  .tag { color: var(--white); font-weight: 700; font-size: 25px; padding: 4px 16px; }
  .tag--navy { background: var(--navy-deep); border-radius: 6px 0 0 6px; }
  .tag--red { background: var(--red); }
  .tag--orange { background: var(--orange); border-radius: 0 6px 6px 0; }

  .badge {
    position: absolute; left: 572px; top: 758px; width: 140px; height: 140px; border-radius: 50%;
    background: var(--white); border: 7px solid var(--orange);
  }

  .footer {
    position: absolute; left: 0; bottom: 0; width: 744px; height: 92px; background: var(--white);
    display: flex; align-items: center; padding: 0 36px;
  }
  .snack .footer { height: 82px; }
  .brand { font-weight: 600; color: var(--ink); font-size: 25px; letter-spacing: 1px; }
  .divider { width: 2px; height: 50px; background: var(--orange); margin: 0 18px; }
  .partner { display: flex; align-items: center; gap: 8px; }
  .partner__dot { width: 18px; height: 18px; border-radius: 50%; background: var(--navy); }
  .partner .brand { font-size: 16px; }
  .address { display: flex; align-items: center; gap: 12px; margin-left: 46px; }
  .address__text { font-weight: 700; font-size: 17px; line-height: 20px; color: var(--ink); }
</style>
</head>
<body>
  <div class="band band--one"></div>
  <div class="band band--two"></div>
  <div class="band band--three"></div>

  <!-- Dinner side, small -->
  <div class="slot slot--small slot--a">
    <article class="poster dinner">
      <div class="poster__ghost" aria-hidden="true">DINNER<br>DINNER</div>
      <div class="poster__photo poster__photo--fondue" role="img" aria-label="Close-up of melted cheese stretching from a baked pasta dish"></div>
      <svg class="headline" viewBox="0 0 744 380" role="heading" aria-level="2" aria-label="What's for dinner tonight?">
        <defs>
          <path id="dinA-1" d="M72,118 Q372,92 672,118"/>
          <path id="dinA-2" d="M40,252 Q372,200 704,252"/>
          <path id="dinA-3" d="M122,348 Q372,326 622,348"/>
        </defs>
        <text class="headline__kicker" font-size="80" textLength="600" lengthAdjust="spacingAndGlyphs"><textPath href="#dinA-1">WHAT'S FOR</textPath></text>
        <text class="headline__hero" font-size="150" textLength="630" lengthAdjust="spacingAndGlyphs"><textPath href="#dinA-2">DINNER</textPath></text>
        <text class="headline__kicker headline__kicker--outlined" font-size="86" textLength="500" lengthAdjust="spacingAndGlyphs"><textPath href="#dinA-3">TONIGHT?</textPath></text>
      </svg>
      <div class="price"><span class="price__label">PRICE</span><span class="price__value"><sup>$</sup>13.50</span></div>
      <ul class="tags"><li class="tag tag--navy">Take &amp; Bake</li><li class="tag tag--red">Baked Pasta</li><li class="tag tag--orange">Lasagna</li></ul>
      <div class="badge" aria-hidden="true"></div>
      <footer class="footer">
        <span class="brand">Calderi pizza</span><span class="divider"></span>
        <span class="partner"><span class="partner__dot"></span><span class="brand">FernLoop</span></span>
        <span class="address"><svg width="26" height="34" viewBox="0 0 26 34"><path d="M13 0C5.8 0 0 5.8 0 13c0 9.5 13 21 13 21s13-11.5 13-21C26 5.8 20.2 0 13 0z" fill="#ef4e23"/><circle cx="13" cy="13" r="5" fill="#fff"/></svg><span class="address__text">Harbour Point Plaza<br>118, 40 2 Street NW</span></span>
      </footer>
    </article>
  </div>

  <!-- Snack side, small -->
  <div class="slot slot--small slot--b">
    <article class="poster snack">
      <div class="poster__ghost" aria-hidden="true">DINNER<br>DINNER</div>
      <div class="poster__photo poster__photo--board" role="img" aria-label="Charcuterie board with crackers, cheese, berries, nuts and cured meats"></div>
      <svg class="headline" viewBox="0 0 744 380" role="heading" aria-level="2" aria-label="Enjoy the flavours of gourmet snacking, all in one convenient box!">
        <defs>
          <path id="snkB-1" d="M112,102 Q372,80 632,106"/>
          <path id="snkB-2" d="M96,198 Q372,168 648,198"/>
          <path id="snkB-3" d="M76,292 Q372,262 668,292"/>
          <path id="snkB-4" d="M110,334 Q390,330 640,292"/>
        </defs>
        <text class="headline__kicker" font-size="36" textLength="520" lengthAdjust="spacingAndGlyphs"><textPath href="#snkB-1">ENJOY THE FLAVOURS OF</textPath></text>
        <text class="headline__hero" font-size="112" textLength="540" lengthAdjust="spacingAndGlyphs"><textPath href="#snkB-2">GOURMET</textPath></text>
        <text class="headline__hero" font-size="112" textLength="580" lengthAdjust="spacingAndGlyphs"><textPath href="#snkB-3">SNACKING</textPath></text>
        <text class="headline__kicker" font-size="30" textLength="525" lengthAdjust="spacingAndGlyphs"><textPath href="#snkB-4">ALL IN ONE CONVENIENT BOX!</textPath></text>
      </svg>
      <div class="price"><span class="price__label">PRICE</span><span class="price__value"><sup>$</sup>8.99</span></div>
      <footer class="footer">
        <span class="brand">Calderi pizza</span><span class="divider"></span>
        <span class="partner"><span class="partner__dot"></span><span class="brand">FernLoop</span></span>
        <span class="address"><svg width="26" height="34" viewBox="0 0 26 34"><path d="M13 0C5.8 0 0 5.8 0 13c0 9.5 13 21 13 21s13-11.5 13-21C26 5.8 20.2 0 13 0z" fill="#ef4e23"/><circle cx="13" cy="13" r="5" fill="#fff"/></svg><span class="address__text">Harbour Point Plaza<br>118, 40 2 Street NW</span></span>
      </footer>
    </article>
  </div>

  <!-- Dinner side, full -->
  <div class="slot slot--c">
    <article class="poster dinner">
      <div class="poster__ghost" aria-hidden="true">DINNER<br>DINNER</div>
      <div class="poster__photo poster__photo--fondue" role="img" aria-label="Close-up of melted cheese stretching from a baked pasta dish"></div>
      <svg class="headline" viewBox="0 0 744 380" role="heading" aria-level="2" aria-label="What's for dinner tonight?">
        <defs>
          <path id="dinC-1" d="M72,118 Q372,92 672,118"/>
          <path id="dinC-2" d="M40,252 Q372,200 704,252"/>
          <path id="dinC-3" d="M122,348 Q372,326 622,348"/>
        </defs>
        <text class="headline__kicker" font-size="80" textLength="600" lengthAdjust="spacingAndGlyphs"><textPath href="#dinC-1">WHAT'S FOR</textPath></text>
        <text class="headline__hero" font-size="150" textLength="630" lengthAdjust="spacingAndGlyphs"><textPath href="#dinC-2">DINNER</textPath></text>
        <text class="headline__kicker headline__kicker--outlined" font-size="86" textLength="500" lengthAdjust="spacingAndGlyphs"><textPath href="#dinC-3">TONIGHT?</textPath></text>
      </svg>
      <div class="price"><span class="price__label">PRICE</span><span class="price__value"><sup>$</sup>13.50</span></div>
      <ul class="tags"><li class="tag tag--navy">Take &amp; Bake</li><li class="tag tag--red">Baked Pasta</li><li class="tag tag--orange">Lasagna</li></ul>
      <div class="badge" aria-hidden="true"></div>
      <footer class="footer">
        <span class="brand">Calderi pizza</span><span class="divider"></span>
        <span class="partner"><span class="partner__dot"></span><span class="brand">FernLoop</span></span>
        <span class="address"><svg width="26" height="34" viewBox="0 0 26 34"><path d="M13 0C5.8 0 0 5.8 0 13c0 9.5 13 21 13 21s13-11.5 13-21C26 5.8 20.2 0 13 0z" fill="#ef4e23"/><circle cx="13" cy="13" r="5" fill="#fff"/></svg><span class="address__text">Harbour Point Plaza<br>118, 40 2 Street NW</span></span>
      </footer>
    </article>
  </div>

  <!-- Snack side, full -->
  <div class="slot slot--d">
    <article class="poster snack">
      <div class="poster__ghost" aria-hidden="true">DINNER<br>DINNER</div>
      <div class="poster__photo poster__photo--board" role="img" aria-label="Charcuterie board with crackers, cheese, berries, nuts and cured meats"></div>
      <svg class="headline" viewBox="0 0 744 380" role="heading" aria-level="2" aria-label="Enjoy the flavours of gourmet snacking, all in one convenient box!">
        <defs>
          <path id="snkD-1" d="M112,102 Q372,80 632,106"/>
          <path id="snkD-2" d="M96,198 Q372,168 648,198"/>
          <path id="snkD-3" d="M76,292 Q372,262 668,292"/>
          <path id="snkD-4" d="M110,334 Q390,330 640,292"/>
        </defs>
        <text class="headline__kicker" font-size="36" textLength="520" lengthAdjust="spacingAndGlyphs"><textPath href="#snkD-1">ENJOY THE FLAVOURS OF</textPath></text>
        <text class="headline__hero" font-size="112" textLength="540" lengthAdjust="spacingAndGlyphs"><textPath href="#snkD-2">GOURMET</textPath></text>
        <text class="headline__hero" font-size="112" textLength="580" lengthAdjust="spacingAndGlyphs"><textPath href="#snkD-3">SNACKING</textPath></text>
        <text class="headline__kicker" font-size="30" textLength="525" lengthAdjust="spacingAndGlyphs"><textPath href="#snkD-4">ALL IN ONE CONVENIENT BOX!</textPath></text>
      </svg>
      <div class="price"><span class="price__label">PRICE</span><span class="price__value"><sup>$</sup>8.99</span></div>
      <footer class="footer">
        <span class="brand">Calderi pizza</span><span class="divider"></span>
        <span class="partner"><span class="partner__dot"></span><span class="brand">FernLoop</span></span>
        <span class="address"><svg width="26" height="34" viewBox="0 0 26 34"><path d="M13 0C5.8 0 0 5.8 0 13c0 9.5 13 21 13 21s13-11.5 13-21C26 5.8 20.2 0 13 0z" fill="#ef4e23"/><circle cx="13" cy="13" r="5" fill="#fff"/></svg><span class="address__text">Harbour Point Plaza<br>118, 40 2 Street NW</span></span>
      </footer>
    </article>
  </div>
</body>
</html>
```